Bref créative
Business card and stationary design for engineering and manufacturing company
Valdorkin Engineering Inc. - (Below) A Pioneer in the Signal Mast Trade Since 1983
Professional
Mark Pellow
2719 North 58th Avenue
Brevmoor, SD 57391
info@valdorkinengineering.example
www.valdorkinengineering.example
I need a business card that I can edit names and email addresses for multiple employees. Check out my logo upload and our website. The stationary is general and will be non-specific to a contact name.

```html
<!DOCTYPE html>
<html lang="en">
<head>
<meta charset="utf-8">
<title>Valdorkin Engineering Inc. – Business Card</title>
<link href="https://fonts.googleapis.com/css2?family=Oswald:wght@600&family=Open+Sans:wght@400;600&display=swap" rel="stylesheet">
<style>
  :root {
    --bg: #e6e6e4;
    --card-dark: #2b2b2b;
    --card-light: #ffffff;
    --ink: #2a2a2a;
    --ink-soft: #555555;
    --orange: #f07f1e;
    --wave-grey: #3a3a3a;
    --rule: #cccccc;
    --white: #ffffff;
  }
  * { margin: 0; padding: 0; box-sizing: border-box; }
  html, body { width: 1200px; height: 864px; overflow: hidden; }
  body {
    background: var(--bg);
    font-family: "Open Sans", Arial, sans-serif;
    position: relative;
  }
  .card {
    position: absolute;
    top: 277px;
    width: 540px;
    height: 310px;
    border-radius: 20px;
    overflow: hidden;
    box-shadow: 0 6px 18px rgba(0,0,0,0.18);
  }
  .card-back { left: 40px; background: var(--card-dark); }
  .card-front { left: 620px; background: var(--card-light); }

  .back-mark {
    position: absolute;
    top: 100px; left: 0; width: 100%;
    text-align: center;
    font-family: "Oswald", Arial, sans-serif;
    font-weight: 600;
    font-size: 64px;
    letter-spacing: 4px;
    color: var(--white);
  }
  .back-web {
    position: absolute;
    top: 196px; left: 0; width: 100%;
    text-align: center;
    font-size: 12px;
    letter-spacing: 1.5px;
    color: var(--white);
  }

  .front-wave { position: absolute; left: 0; bottom: 0; width: 540px; height: 110px; }
  .logo-square {
    position: absolute;
    left: 36px; top: 62px;
    width: 58px; height: 58px;
    background: var(--orange);
  }
  .company-name {
    position: absolute;
    left: 106px; top: 58px;
    width: 170px;
    font-family: "Oswald", Arial, sans-serif;
    font-weight: 600;
    font-size: 21px;
    line-height: 1.05;
    text-transform: uppercase;
    color: var(--ink);
  }
  .divider {
    position: absolute;
    left: 280px; top: 58px;
    width: 1px; height: 120px;
    background: var(--rule);
  }
  .contact-name {
    position: absolute;
    left: 36px; top: 140px;
    font-size: 15px;
    font-weight: 600;
    color: var(--orange);
  }
  .contact-list {
    position: absolute;
    left: 292px; top: 60px;
    list-style: none;
  }
  .contact-list li {
    display: flex; align-items: center;
    height: 21px;
    font-size: 11px;
    color: var(--ink-soft);
    white-space: nowrap;
  }
  .contact-list svg { width: 14px; height: 14px; margin-right: 7px; flex: none; }
  .address {
    position: absolute;
    left: 36px; top: 196px;
    font-size: 11.5px;
    line-height: 1.45;
    color: var(--ink-soft);
  }
</style>
</head>
<body>

<section class="card card-back" aria-label="Business card back">
  <div class="back-mark">VEI</div>
  <div class="back-web">www.valdorkinengineering.example</div>
</section>

<section class="card card-front" aria-label="Business card front">
  <div class="logo-square"></div>
  <div class="company-name">Valdorkin Engineering Inc.</div>
  <div class="divider"></div>
  <div class="contact-name">Mark Pellow</div>

  <ul class="contact-list">
    <li><svg viewBox="0 0 14 14"><circle cx="7" cy="7" r="7" fill="var(--orange)"/><path d="M4.5 3.8l1.4-.3.8 1.8-.9.7c.5 1 1.2 1.7 2.2 2.2l.7-.9 1.8.8-.3 1.4c-3.2.2-5.9-2.5-5.7-5.7z" fill="#fff"/></svg>800-555-0142</li>
    <li><svg viewBox="0 0 14 14"><circle cx="7" cy="7" r="7" fill="var(--orange)"/><path d="M4.5 3.8l1.4-.3.8 1.8-.9.7c.5 1 1.2 1.7 2.2 2.2l.7-.9 1.8.8-.3 1.4c-3.2.2-5.9-2.5-5.7-5.7z" fill="#fff"/></svg>605-555-0187</li>
    <li><svg viewBox="0 0 14 14"><circle cx="7" cy="7" r="7" fill="var(--orange)"/><rect x="4" y="4.5" width="6" height="5" fill="#fff"/></svg>605-555-0163</li>
    <li><svg viewBox="0 0 14 14"><circle cx="7" cy="7" r="7" fill="var(--orange)"/><rect x="3.8" y="4.6" width="6.4" height="4.8" fill="#fff"/><path d="M3.8 4.6L7 7.2l3.2-2.6" stroke="var(--orange)" stroke-width=".8" fill="none"/></svg>info@valdorkinengineering.example</li>
    <li><svg viewBox="0 0 14 14"><circle cx="7" cy="7" r="7" fill="var(--orange)"/><circle cx="7" cy="7" r="3.2" fill="none" stroke="#fff" stroke-width="1"/><path d="M3.8 7h6.4" stroke="#fff" stroke-width=".8"/></svg>www.valdorkinengineering.example</li>
  </ul>

  <div class="address">2719 North 58th Avenue<br>Brevmoor, SD 57391</div>

  <svg class="front-wave" viewBox="0 0 540 110" preserveAspectRatio="none" aria-hidden="true">
    <path d="M0 92 C140 60 300 110 540 30 L540 110 L0 110 Z" fill="var(--orange)"/>
    <path d="M0 100 C150 74 310 118 540 44" stroke="var(--wave-grey)" stroke-width="3" fill="none"/>
  </svg>
</section>

</body>
</html>
```